Bref créative
Valmirock Stationary Design
Business Cards, Letterhead, etc....
Professional
Dorian K. Pelletrow
Chief Executive Officer
2718 N. Birch Ln.
Suite K-42
Tempe, AZ 85107-3318
XXX-XXX-XXXX
dorian@valmirock-example.com
http://www.valmirock-example.com/
See our website for our business areas and marketing information.
Back of the business card should be branded, but simple. Maybe our company monogram. There should be enough space to write notes on the back of the card.
Contains several versions of our logo for stationary design.

```html
<!DOCTYPE html>
<html lang="en">
<head>
<meta charset="utf-8">
<title>Valmirock Stationery</title>
<link rel="stylesheet" href="https://fonts.googleapis.com/css2?family=Open+Sans:wght@400;600;700&display=swap">
<style>
  :root {
    --backdrop: #8a5a34;
    --paper: #fbfbfc;
    --band: #6d80aa;
    --band-dark: #55689a;
    --band-light: #9aa9c9;
    --brand: #2d4e86;
    --ink: #4a4f5c;
    --muted: #8b90a0;
    --mark: #e4e7ee;
  }
  * { margin: 0; padding: 0; box-sizing: border-box; }
  html, body { width: 1200px; height: 499px; overflow: hidden; }
  body {
    position: relative;
    background: var(--backdrop);
    font-family: "Open Sans", Arial, sans-serif;
    color: var(--ink);
  }
  .sheet {
    position: absolute;
    background: var(--paper);
    overflow: hidden;
    box-shadow: 0 3px 8px rgba(0,0,0,.35);
  }
  .sheet svg.band { position: absolute; left: 0; bottom: 0; width: 100%; }
  .brand {
    position: absolute;
    display: flex;
    align-items: center;
    gap: 5px;
  }
  .brand-dot { border-radius: 50%; background: var(--band); }
  .brand-name {
    font-weight: 700;
    color: var(--brand);
    letter-spacing: .5px;
    text-transform: uppercase;
    line-height: 1;
  }
  .brand-tag {
    position: absolute;
    color: var(--muted);
    font-size: 4px;
    letter-spacing: .3px;
  }
  .faint-mark { position: absolute; border-radius: 50%; background: var(--mark); }
  .small-text { position: absolute; font-size: 4.5px; line-height: 1.45; color: var(--ink); }
  .on-band { color: #eef1f8; }

  .letterhead { left: 12px; top: 22px; width: 228px; height: 458px; }
  .envelope-back { left: 460px; top: 82px; width: 282px; height: 104px; background: #f1f2f5; }
  .envelope-front { left: 480px; top: 228px; width: 283px; height: 144px; }
  .card { width: 269px; }
  .card-front { left: 907px; top: 24px; height: 156px; }
  .card-contact { left: 907px; top: 192px; height: 139px; }
  .card-back { left: 907px; top: 348px; height: 144px; background: var(--band); }
</style>
</head>
<body>

  <!-- Letterhead -->
  <section class="sheet letterhead" aria-label="Letterhead">
    <div class="brand" style="left:18px; top:22px;">
      <span class="brand-dot" style="width:9px;height:9px;"></span>
      <span class="brand-name" style="font-size:10px;">Valmirock</span>
    </div>
    <div class="brand-tag" style="left:32px; top:34px;">Stationery Design Group</div>
    <div class="faint-mark" role="img" aria-label="Faint brand circle" style="left:150px; top:320px; width:70px; height:70px;"></div>
    <svg class="band" viewBox="0 0 228 80" height="80" preserveAspectRatio="none">
      <path d="M0 45 Q 90 -5 228 20 L228 80 L0 80 Z" fill="var(--band-light)"/>
      <path d="M0 55 Q 100 5 228 28 L228 80 L0 80 Z" fill="var(--band)"/>
    </svg>
    <div class="small-text on-band" style="left:60px; bottom:12px; text-align:left;">
      2718 N. Birch Ln., Suite K-42 &nbsp; Tempe, AZ 85107-3318<br>
      P: XXX-XXX-XXXX &nbsp; F: XXX-XXX-XXXX &nbsp; W: www.valmirock-example.com
    </div>
  </section>

  <!-- Envelope back -->
  <section class="sheet envelope-back" aria-label="Envelope back">
    <svg viewBox="0 0 282 104" width="282" height="104" style="position:absolute;left:0;top:0;">
      <path d="M0 0 L282 0 L282 8 Q141 95 0 8 Z" fill="var(--band)"/>
      <path d="M0 8 Q141 95 282 8" fill="none" stroke="var(--band-dark)" stroke-width="1"/>
    </svg>
    <div class="faint-mark" role="img" aria-label="Faint brand circle" style="left:124px; top:14px; width:34px; height:34px; background:#8e9dc0;"></div>
  </section>

  <!-- Envelope front -->
  <section class="sheet envelope-front" aria-label="Envelope front">
    <div class="brand" style="left:14px; top:16px;">
      <span class="brand-dot" style="width:8px;height:8px;"></span>
      <span class="brand-name" style="font-size:9px;">Valmirock</span>
    </div>
    <div class="brand-tag" style="left:27px; top:27px;">Stationery Design Group</div>
    <div class="faint-mark" role="img" aria-label="Faint brand circle" style="left:150px; top:55px; width:62px; height:62px;"></div>
    <svg class="band" viewBox="0 0 283 50" height="50" preserveAspectRatio="none">
      <path d="M0 50 Q 130 -5 283 10 L283 50 Z" fill="var(--band-light)"/>
      <path d="M30 50 Q 150 8 283 18 L283 50 Z" fill="var(--band)"/>
    </svg>
    <div class="small-text" style="left:226px; top:60px;">
      2718 N. Birch Ln.<br>Suite K-42<br>Tempe, AZ 85107-3318
    </div>
  </section>

  <!-- Business card front -->
  <section class="sheet card card-front" aria-label="Business card front">
    <div class="faint-mark" role="img" aria-label="Faint brand circle" style="left:10px; top:10px; width:60px; height:60px;"></div>
    <svg class="band" viewBox="0 0 269 60" height="60" preserveAspectRatio="none">
      <path d="M0 60 Q 120 0 269 10 L269 60 Z" fill="var(--band-light)"/>
      <path d="M20 60 Q 140 10 269 20 L269 60 Z" fill="var(--band)"/>
    </svg>
  </section>

  <!-- Business card with contact details -->
  <section class="sheet card card-contact" aria-label="Business card contact side">
    <div class="brand" style="left:14px; top:16px;">
      <span class="brand-dot" style="width:8px;height:8px;"></span>
      <span class="brand-name" style="font-size:9px;">Valmirock</span>
    </div>
    <div class="brand-tag" style="left:27px; top:27px;">Stationery Design Group</div>
    <div class="small-text" style="left:14px; top:60px;">
      <strong style="font-size:5.5px;">Dorian K. Pelletrow</strong><br>Chief Executive Officer
    </div>
    <div class="small-text" style="left:14px; top:82px;">
      dorian@valmirock-example.com<br>http://www.valmirock-example.com/
    </div>
    <div class="small-text" style="left:190px; top:60px;">
      2718 N. Birch Ln.<br>Suite K-42<br>Tempe, AZ 85107-3318<br>XXX-XXX-XXXX
    </div>
    <svg class="band" viewBox="0 0 269 30" height="30" preserveAspectRatio="none">
      <path d="M0 30 Q 130 -4 269 8 L269 30 Z" fill="var(--band)"/>
    </svg>
  </section>

  <!-- Business card back -->
  <section class="sheet card card-back" aria-label="Business card back">
    <div class="faint-mark" role="img" aria-label="Faint brand circle" style="left:14px; top:14px; width:52px; height:52px; background:#8294bb;"></div>
  </section>

</body>
</html>
```